Card Design Project

We are looking for a couple card / box designs that will for a new company that is in the bereavement assistance industry.
Our customers are churches, counseling centers and funeral homes.
Once we have these card designs we will need to work with that same artist to help us out with box graphic designs that are similar to the card designs. The box is 12" long x 4" wide x 6" high
We will need more designs in the future so we are looking for an artist for future work.
Our look needs to be professional and solemn.
The front of the card should be quite close to what i am attaching but with some professional touches to it that give it a proper look. We dont want you to stray to far from what i have attached but if you feel you have some good ideas we would be more than happy to see them.
The back of the card we want people to be able to leave the family a note so will need wording such as "leave a message to the family" or "write a memory"
Keep in mind we will need this look to be able to match graphics on the box as well, we kind of need the card design and box design to go together.
Thanks
Just wanted to mention to all designers that although we would like our logo on the card it is something that we need to keep kind of in the background somehow. We cant be seen as trying to push a brand name too much so please keep that in mind. Thanks
Reason: HOLIDAY
Designers, I took the need to see what the design looked like on a box out.
Reason: just need a bit of extra time guys, thanks for all who are helping us on this!
Target Market(s)
Funeral homes, churches, counseling centers
Industry/Entity Type
Industry
Requirements
Must have
- Professional and solemn look
Card need to be 4"wide X 6" high and needs to be portrait
A pin will be attached to the top right part of the card so will need a space there for it.
I was thinking that we would have the pic of the ribbon symbol there so when the pin is off the card there would still be a ribbon pic there. The pins that we will be attaching are ribbon pins similar to what i have on my pdf's
Please keep in mind that we cant really have out logo in a dominant area on the card. We would like to have it subtly in there but not to where it is in your face type of thing.
Nice to have
- Our logo but very small, not to intrusive .
Would like 2 designs, one dark and another light.
Maybe 1 masculine or gender neutral and another feminine
Wording should be the same

```html
<!DOCTYPE html>
<html lang="en">
<head>
<meta charset="utf-8">
<title>Memorial Cards – Light and Dark</title>
<link href="https://fonts.googleapis.com/css2?family=Source+Sans+3:ital,wght@0,400;1,300&display=swap" rel="stylesheet">
<style>
  :root {
    --page: #ffffff;
    --ink-dark: #2b2b2b;
    --ink-light: #f2f2f2;
    --rule: #7a7a7a;
    --mark: #8a8a8a;
    --pin-spot-light: rgba(120,120,120,0.35);
    --pin-spot-dark: rgba(150,150,150,0.45);
    --shadow: rgba(0,0,0,0.28);
  }
  * { margin: 0; padding: 0; box-sizing: border-box; }
  html, body { width: 1200px; height: 828px; overflow: hidden; background: var(--page); }
  body { position: relative; font-family: "Source Sans 3", Arial, sans-serif; }

  .card {
    position: absolute;
    width: 561px;
    height: 374px;
    box-shadow: 0 1px 4px var(--shadow);
    overflow: hidden;
  }
  .card--front-light { left: 34px; top: 36px; }
  .card--back-light  { left: 606px; top: 36px; }
  .card--front-dark  { left: 34px; top: 418px; }
  .card--back-dark   { left: 606px; top: 418px; }

  .card__photo { position: absolute; inset: 0; }
  .card--front-light .card__photo {
    background:
      radial-gradient(ellipse 45% 55% at 80% 62%, rgba(255,255,255,0.75) 0%, rgba(255,255,255,0) 100%),
      radial-gradient(ellipse at 60% 55%, #e6e6e6 0%, #d2d2d2 55%, #b4b4b4 100%);
  }
  .card--back-light .card__photo {
    background:
      radial-gradient(ellipse 40% 55% at 28% 70%, rgba(236,236,236,0.9) 0%, rgba(236,236,236,0) 100%),
      radial-gradient(ellipse at 55% 50%, #fbfbfb 0%, #f3f3f3 55%, #e4e4e4 100%);
  }
  .card--front-dark .card__photo {
    background:
      radial-gradient(ellipse 18% 70% at 72% 70%, rgba(170,170,170,0.55) 0%, rgba(170,170,170,0) 100%),
      radial-gradient(ellipse 12% 40% at 75% 12%, rgba(220,220,220,0.7) 0%, rgba(220,220,220,0) 100%),
      linear-gradient(90deg, #000 0%, #000 52%, #141414 62%, #3a3a3a 72%, #1c1c1c 80%, #050505 88%, #000 100%);
  }
  .card--back-dark .card__photo {
    background:
      radial-gradient(ellipse 20% 80% at 40% 40%, rgba(250,250,250,0.8) 0%, rgba(250,250,250,0) 100%),
      linear-gradient(90deg, #dcdcdc 0%, #e2e2e2 25%, #ececec 45%, #e4e4e4 65%, #dadada 100%);
  }

  .pin-spot {
    position: absolute;
    left: 439px;
    top: 20px;
    width: 79px;
    height: 99px;
  }
  .card--front-light .pin-spot { background: var(--pin-spot-light); }
  .card--front-dark .pin-spot { background: var(--pin-spot-dark); }

  .message { position: absolute; left: 49px; top: 46px; width: 250px; height: 300px; }
  .message__greeting {
    font-weight: 300;
    font-style: italic;
    font-size: 34px;
    line-height: 40px;
    margin-bottom: 22px;
  }
  .message__para {
    font-size: 13px;
    line-height: 16px;
    margin-bottom: 15px;
  }
  .message__closing {
    position: absolute;
    top: 253px;
    font-size: 13px;
    line-height: 16px;
  }
  .card--front-light .message { color: var(--ink-dark); }
  .card--front-dark .message { color: var(--ink-light); }

  .memory__title {
    position: absolute;
    left: 0; right: 0;
    top: 74px;
    text-align: center;
    font-weight: 300;
    font-style: italic;
    font-size: 22px;
    color: var(--ink-dark);
  }
  .memory__lines {
    position: absolute;
    left: 61px;
    top: 103px;
    width: 438px;
    list-style: none;
  }
  .memory__lines li {
    height: 26px;
    border-bottom: 1px solid var(--rule);
  }
  .signature {
    position: absolute;
    left: 0; right: 0;
    top: 294px;
    display: flex;
    flex-direction: column;
    align-items: center;
    gap: 3px;
  }
  .signature__square { width: 38px; height: 36px; background: var(--pin-spot-light); }
  .signature__name {
    font-size: 8px;
    line-height: 8px;
    letter-spacing: 0.3px;
    text-align: center;
    text-transform: uppercase;
    color: var(--mark);
  }
</style>
</head>
<body>

  <section class="card card--front-light">
    <div class="card__photo" role="img" aria-label="Soft grey textured background with a white daisy and scattered petals"></div>
    <div class="pin-spot" aria-label="Space for the ribbon pin"></div>
    <div class="message">
      <h2 class="message__greeting">Dear Friends</h2>
      <p class="message__para">Your support in attending this memorial and<br>celebration of life means so much to us.</p>
      <p class="message__para">Our loved one has touched you in ways we<br>may not even recognize yet.</p>
      <p class="message__para">We invite you to wear this pin through your<br>grieving process, which we receive as a symbol<br>of your sympathy and support of our loss</p>
      <p class="message__closing">Thank you for grieving<br>together with us</p>
    </div>
  </section>

  <section class="card card--back-light">
    <div class="card__photo" role="img" aria-label="Faded white daisy on a pale background"></div>
    <h3 class="memory__title">share a memory</h3>
    <ul class="memory__lines"><li></li><li></li><li></li><li></li><li></li><li></li></ul>
    <div class="signature">
      <span class="signature__square"></span>
      <span class="signature__name">Kindred<br>Hours</span>
    </div>
  </section>

  <section class="card card--front-dark">
    <div class="card__photo" role="img" aria-label="Dark forest path with light rays falling through the trees"></div>
    <div class="pin-spot" aria-label="Space for the ribbon pin"></div>
    <div class="message">
      <h2 class="message__greeting">Dear Friends</h2>
      <p class="message__para">Your support in attending this memorial and<br>celebration of life means so much to us.</p>
      <p class="message__para">Our loved one has touched you in ways we<br>may not even recognize yet.</p>
      <p class="message__para">We invite you to wear this pin through your<br>grieving process, which we receive as a symbol<br>of your sympathy and support of our loss</p>
      <p class="message__closing">Thank you for grieving<br>together with us</p>
    </div>
  </section>

  <section class="card card--back-dark">
    <div class="card__photo" role="img" aria-label="Faded forest path with light rays on a pale grey background"></div>
    <h3 class="memory__title">share a memory</h3>
    <ul class="memory__lines"><li></li><li></li><li></li><li></li><li></li><li></li></ul>
    <div class="signature">
      <span class="signature__square"></span>
      <span class="signature__name">Kindred<br>Hours</span>
    </div>
  </section>

</body>
</html>
```